Flyer für Bürgerenergiegemeinschaft
Zielgruppe
Als Bürgerenergiegemeinschaft sind wir für unsere Bürgerinnen und Bürger die erste Anlaufstelle wenn es um sauberen regionalen erneuerbaren Strom geht. Mehr Infos unter www.kwl-rax.example
Aufgabenstellung
Ziel soll ein Falzflyer DL (220x110mm) mit Wickelfalz von Drucklo (https://www.drucklomat.example/marketingmaterial/falzflyer) sein. Bitte daher die Designrichtlinien von Drucklo beachten. Ausgefaltet hat der Flyer dann 297x210mm, gefaltet 99x210mm. Somit sind 6 kleine Seiten zu befüllen.
Auf diesen 6 Seiten soll der Inhalt unserer Webseite www.kwl-rax.example im gleichen Look übersichtlich aufbereitet werden.
Auf der gefalteten Rückseite sollen im unterne Bereich die nicht ausgefüllten Felder des Online-Rechners sein,
damit man im Kundengespräch die Werte die der Rechner ausgibt auf den Flyer niederschreiben kann den der Kunde dann mitbekommt.
Bilder können von der Webseite geladen werden oder von uns zur Verfügung gestellt werden.

```html
<!DOCTYPE html>
<html lang="de">
<head>
<meta charset="utf-8">
<title>KWLRAX Falzflyer</title>
<link href="https://fonts.googleapis.com/css2?family=Poppins:ital,wght@0,400;0,500;0,600;0,700;0,800;1,400&display=swap" rel="stylesheet">
<style>
:root{
  --navy:#1f3d78;
  --blue:#1690d8;
  --sky:#2aa3e3;
  --ink:#1d2433;
  --grey:#555b66;
  --paper:#ffffff;
  --bg:#e9ebee;
  --photo-sky:#8fb2d4;
  --photo-green:#5c7a4a;
}
*{box-sizing:border-box;margin:0;padding:0}
html,body{width:803px;height:1200px;overflow:hidden;background:var(--bg);font-family:"Poppins",sans-serif;color:var(--ink)}
.spread{position:absolute;left:20px;width:763px;height:540px;background:var(--paper);overflow:hidden;box-shadow:0 2px 8px rgba(0,0,0,.18)}
.spread.outside{top:40px}
.spread.inside{top:620px}
.spread > svg.bg{position:absolute;left:0;top:0}
.abs{position:absolute}
.kicker{font-size:7.5px;text-transform:uppercase;letter-spacing:.2px}
.kicker.blue{color:var(--blue)}
.kicker.light{color:#7fc6f0}
.h{font-weight:700;line-height:1.2}
.small{font-size:7px;line-height:1.45;color:var(--grey)}
.brand{font-weight:700;letter-spacing:.5px;display:flex;align-items:center;gap:7px}
.brand .dot{display:inline-block;border-radius:50%;border:3px solid currentColor}
.web{color:#fff;font-weight:700;font-size:15px;text-align:center}
.checks{border:1px solid var(--blue);display:grid;grid-template-columns:1.2fr 1fr;gap:6px 6px;padding:8px 10px;font-size:7px;color:var(--grey);background:#fff}
.checks span::before,.tick::before{content:"";display:inline-block;width:6px;height:6px;border-radius:50%;background:var(--blue);margin-right:4px;vertical-align:middle}
.mail{display:flex;gap:8px;align-items:center;color:#fff;font-size:7px;line-height:1.3}
.mail svg{flex:none}
.stat{position:absolute;top:395px;width:68px;height:75px;text-align:center;color:#fff;font-size:6px}
.stat b{display:block;font-size:18px;line-height:1.1;font-weight:800}
.stat .ic{width:26px;height:26px;border-radius:50%;background:var(--blue);border:2px solid #fff;margin:-13px auto 4px}
.item{position:absolute;left:30px;width:210px;display:flex;gap:10px}
.item .sq{flex:none;width:22px;height:22px;background:var(--blue)}
.item .t{font-size:8px;font-weight:700;color:var(--ink)}
.item .small{font-size:6.5px;line-height:1.4}
.svc{position:absolute;width:108px;height:36px;border:1.5px solid var(--blue);display:flex;align-items:flex-end;justify-content:center;padding-bottom:5px;font-size:6.5px;font-weight:700;background:#fff}
.svc::before{content:"";position:absolute;top:-11px;left:50%;width:20px;height:20px;margin-left:-10px;background:var(--blue);transform:rotate(45deg);border:2px solid #fff}
.req{position:absolute;left:540px;width:200px;display:flex;gap:12px;color:#fff}
.req .sq{flex:none;width:26px;height:26px;background:var(--blue);transform:rotate(45deg) scale(.85)}
.req .t{font-size:8px;font-weight:700}
.req .small{color:#d3e4f5}
</style>
</head>
<body>

<section class="spread outside">
  <svg class="bg" width="763" height="540" viewBox="0 0 763 540">
    <path d="M0 185 Q127 165 254 180 L254 250 Q127 225 0 245 Z" fill="var(--blue)"/>
    <path d="M0 245 Q127 225 254 250 L254 490 L0 490 Z" fill="#b9894f" role="img" aria-label="Foto: Solarmodule an einer Gebäudefassade"/>
    <rect x="0" y="490" width="254" height="50" fill="var(--navy)"/>
    <path d="M254 0 L509 0 L509 185 Q400 150 254 135 Z" fill="var(--photo-green)" role="img" aria-label="Foto: Ortschaft mit Kirche in hügeliger Landschaft"/>
    <path d="M254 135 Q400 150 509 185 L509 200 Q400 165 254 150 Z" fill="var(--navy)"/>
    <path d="M254 480 L509 470 L509 540 L254 540 Z" fill="var(--blue)"/>
    <path d="M254 490 Q300 505 330 540 L254 540 Z" fill="var(--navy)"/>
    <rect x="509" y="0" width="254" height="540" fill="var(--sky)"/>
    <path d="M509 0 L763 0 L763 60 Q640 75 509 60 Z" fill="#fff"/>
    <circle cx="636" cy="252" r="100" fill="#fff"/>
    <circle cx="636" cy="252" r="94" fill="var(--photo-sky)" role="img" aria-label="Foto: Monteure installieren ein Solarmodul auf einem Dach"/>
    <path d="M509 470 Q600 500 763 480 L763 540 L509 540 Z" fill="var(--navy)"/>
  </svg>

  <div class="abs" style="left:28px;top:22px;width:200px">
    <div class="kicker" style="color:var(--ink)">Über uns</div>
    <div class="h" style="font-size:9.5px">Bürgerenergiegemeinschaft<br>Talheim an der Lenna</div>
    <p class="small" style="margin-top:10px">Als Bürgerenergiegemeinschaft sind wir für unsere Bürgerinnen und Bürger die erste Anlaufstelle wenn es um sauberen regionalen erneuerbaren Strom geht.</p>
  </div>
  <div class="checks abs" style="left:28px;top:128px;width:190px">
    <span>Grüne Energie</span><span>Faire Preise</span>
    <span>Regional produziert</span><span>Für jeden</span>
  </div>
  <div class="mail abs" style="left:28px;top:197px">
    <svg width="22" height="16" viewBox="0 0 22 16"><rect x="1" y="1" width="20" height="14" fill="none" stroke="#fff" stroke-width="1.5"/><path d="M1 1 L11 9 L21 1" fill="none" stroke="#fff" stroke-width="1.5"/></svg>
    <div>Schicken Sie uns gerne eine E-Mail<br>wenn Sie Fragen haben<br><b>info@kwl-rax.example</b></div>
  </div>
  <div class="web abs" style="left:0;top:505px;width:254px;font-size:13px">www.kwl-rax.example</div>

  <div class="abs" style="left:280px;top:218px;width:205px">
    <div class="kicker" style="color:var(--ink)">Online Rechner</div>
    <div class="h" style="font-size:9px">Dient zur einfachen Kostenabschätzung</div>
    <div style="display:flex;justify-content:space-between;margin:12px 0;font-size:7px;color:var(--grey)">
      <span class="tick">Direkt-Ergebnis</span><span class="tick">Komplett unverbindlich</span>
    </div>
    <p class="small">Wir stellen Ihnen hier eine einfache Möglichkeit zur Verfügung die Sinnhaftigkeit eines Beitritts in die BEG durchzurechnen.</p>
    <p class="small" style="margin-top:8px">Die Berechnung basiert auf 2 Cent/kWh Gemeinschaftskosten und einem Netzentgeld inkl. Abgaben von 6,9588 Cent/kWh (welches vom Regionalnetz verrechnet wird).</p>
    <p class="small" style="margin-top:8px">Nicht notwendige Felder für die jeweilige Berechnung einfach nicht befüllen.</p>
    <div style="border-top:1px solid #ccd;margin-top:20px;padding-top:8px;font-size:7px;font-weight:700;line-height:1.8">
      <div><span class="tick"></span>info@kwl-rax.example</div>
      <div><span class="tick"></span>www.kwl-rax.example</div>
      <div><span class="tick"></span>Lindenweg 12 2651 Tal</div>
    </div>
  </div>
  <div class="brand abs" style="left:254px;top:496px;width:255px;justify-content:center;color:#fff;font-size:22px">
    <span class="dot" style="width:20px;height:20px"></span>KWLRAX
  </div>

  <div class="brand abs" style="left:509px;top:14px;width:254px;justify-content:center;color:var(--blue);font-size:24px">
    <span class="dot" style="width:22px;height:22px"></span>KWLRAX
  </div>
  <div class="abs" style="left:509px;top:78px;width:254px;text-align:center;color:#fff">
    <div style="font-size:7.5px;line-height:1.35">BÜRGERENERGIEGEMEINSCHAFT<br>TALHEIM AN DER LENNA</div>
    <div class="h" style="font-size:18px;margin-top:5px">Regionaler Strom<br>für jeden!</div>
  </div>
  <div class="stat" style="left:525px;background:var(--blue)"><div class="ic"></div>Zählpunkte<b>20+</b></div>
  <div class="stat" style="left:602px;background:#fff;color:var(--navy)"><div class="ic"></div>PV Leistung<b>&gt;100</b><span style="font-size:9px;font-weight:700">kWp</span></div>
  <div class="stat" style="left:679px;background:var(--blue)"><div class="ic"></div>Verteilte Energie<b style="font-size:10px">Testphase</b></div>
  <div class="web abs" style="left:509px;top:505px;width:254px;font-size:13px">www.kwl-rax.example</div>
</section>

<section class="spread inside">
  <svg class="bg" width="763" height="540" viewBox="0 0 763 540">
    <path d="M0 450 Q130 490 254 470 L254 540 L0 540 Z" fill="var(--navy)"/>
    <circle cx="100" cy="432" r="92" fill="var(--blue)"/>
    <circle cx="100" cy="432" r="86" fill="#6f8fb0" role="img" aria-label="Foto: Industrieanlage mit Stahlgerüst und Tank"/>
    <path d="M254 430 Q380 420 509 380 L509 540 L254 540 Z" fill="var(--blue)"/>
    <path d="M254 500 Q380 500 509 470 L509 540 L254 540 Z" fill="#fff"/>
    <rect x="509" y="0" width="254" height="200" fill="var(--photo-sky)" role="img" aria-label="Foto: Reinigung von Solarmodulen auf einem Freiflächen-Solarpark"/>
    <path d="M509 210 Q620 185 763 160 L763 540 L509 540 Z" fill="var(--blue)"/>
    <path d="M509 225 Q620 200 763 180 L763 540 L509 540 Z" fill="var(--navy)"/>
  </svg>

  <div class="abs" style="left:28px;top:22px;width:205px">
    <div class="kicker blue">Warum sollten Sie bei uns Kunde werden?</div>
    <div class="h" style="font-size:11px;color:var(--navy)">Wir helfen Ihnen Ihre Stromkosten zu senken und dabei etwas Gutes für die Umwelt zu tun</div>
  </div>
  <div class="item" style="top:102px"><div class="sq"></div><div><div class="t">PV Anlagen Besitzer</div><div class="small">Als Anlagenbesitzer mit Einspeisung bekommen Sie bei uns bessere Preise als bei einer Einspeisung zum Marktpreis</div></div></div>
  <div class="item" style="top:150px"><div class="sq"></div><div><div class="t">Stromverteilung neu durchdacht</div><div class="small">Der Strom bleibt innerhalb der Gemeinschaft und es ist somit jederzeit nachvollziehbar woher dieser kommt</div></div></div>
  <div class="item" style="top:198px"><div class="sq"></div><div><div class="t">Kunden ohne PV Anlage</div><div class="small">Durch die Energiegemeinschaft beziehen Sie grünen regionalen Strom zu reduzierten Kosten</div></div></div>
  <div class="item" style="top:240px"><div class="sq"></div><div><div class="t">Kleines Team</div><div class="small">Durch unsere schlanke Organisation kommen wir mit geringen Overhead-Kosten für den Strombezieher aus</div></div></div>

  <div class="abs" style="left:278px;top:22px;width:210px">
    <div class="kicker blue">Unser Service für Sie</div>
    <div class="h" style="font-size:11px;color:var(--navy)">Energiegemeinschaft auf neuem Level</div>
  </div>
  <div class="svc" style="left:270px;top:92px">Anmeldungen</div>
  <div class="svc" style="left:387px;top:92px">Transparenz</div>
  <div class="svc" style="left:270px;top:152px">SEPA Lastschrift</div>
  <div class="svc" style="left:387px;top:152px">Einspeisevertrag</div>
  <div class="svc" style="left:270px;top:212px">Bürgerenergiegemeinschaft</div>
  <div class="svc" style="left:387px;top:212px">Bezugsvertrag</div>
  <div class="svc" style="left:270px;top:272px">Energieeinspeisung</div>
  <div class="svc" style="left:387px;top:272px">Gemeinschaftskosten</div>
  <div class="svc" style="left:328px;top:332px">Energieabnahme</div>
  <div class="brand abs" style="left:254px;top:448px;width:255px;justify-content:center;color:#fff;font-size:24px">
    <span class="dot" style="width:22px;height:22px"></span>KWLRAX
  </div>
  <div class="mail abs" style="left:285px;top:505px;color:var(--navy)">
    <svg width="22" height="16" viewBox="0 0 22 16"><rect x="1" y="1" width="20" height="14" fill="none" stroke="var(--blue)" stroke-width="1.5"/><path d="M1 1 L11 9 L21 1" fill="none" stroke="var(--blue)" stroke-width="1.5"/></svg>
    <div>Schicken Sie uns gerne eine E-Mail<br>wenn Sie Fragen haben<br><b>info@kwl-rax.example</b></div>
  </div>

  <div class="abs" style="left:530px;top:240px;width:215px;color:#fff">
    <div class="kicker light">Beitritt in die Energiegemeinschaft</div>
    <div class="h" style="font-size:11px">Folgende Voraussetzungen müssen für den Beitritt erfüllt sein</div>
  </div>
  <div class="req" style="top:320px"><div class="sq"></div><div><div class="t">Netzgebiet</div><div class="small">Um Teil unserer BEG zu werden müssen Sie im Regionalnetz angeschlossen sein</div></div></div>
  <div class="req" style="top:378px"><div class="sq"></div><div><div class="t">Smart Meter + Opt-In</div><div class="small">Damit wir Ihre Einspeisung/Bezug erfassen können muss ein kommunikativer SmartMeter inkl. 15min Opt-In verbaut sein.</div></div></div>
  <div class="req" style="top:450px"><div class="sq"></div><div><div class="t">SmartMeter Portal</div><div class="small">Bestehender Login um uns die Freigabe auf Ihre Daten zu erteilen</div></div></div>
</section>

</body>
</html>
```